"On the Air" Sign for our podcast studio

We need a sign that says "QTRM <<logo>> is On The Air."

Would like this to be two color (black and red.) Ideally in an art deco style. We are going to use this sign on an interior wall to our studio to let people know when the studio is in use, so it should be noticeable right away.

The intention is to have this sign fabricated in a transparent material with the foreground in opaque black and the background in transparent red to show light through it, or we would consider a black opaque background with a red transparent design.

I've attached some examples to show purpose.

Target Market(s)

Fans of this websites - https://marrowfieldpartners.com

Industry/Entity Type

Aviation industry

Font styles to use
Decorative

Colors
EB3D1F
EC4F4E
F09395
F8D3D4
FCEDEE

Requirements
Must have
• The included logo, and the words "On the Air."
Nice to have
• Art Deco style
Should not have
• Anything that could not be used in a transparent sign that lights up from behind.

```html
<!DOCTYPE html>
<html lang="en">
<head>
<meta charset="utf-8">
<title>QTRM On The Air Sign</title>
<link rel="stylesheet" href="https://fonts.googleapis.com/css2?family=Titan+One&display=swap">
<style>
  :root {
    --page-bg: #ffffff;
    --sign-red: #d40000;
    --sign-red-light: #e81a14;
    --sign-edge: #b00000;
    --letter-fill: #fbf3f3;
    --letter-stroke: #b30000;
    --glow: rgba(255, 220, 220, 0.85);
  }
  * { margin: 0; padding: 0; box-sizing: border-box; }
  html, body {
    width: 1200px;
    height: 1199px;
    overflow: hidden;
    background: var(--page-bg);
  }
  .canvas {
    position: relative;
    width: 1200px;
    height: 1199px;
  }
  .sign {
    position: absolute;
    left: 222px;
    width: 763px;
    height: 225px;
    border: 2px solid var(--sign-edge);
    border-radius: 3px;
    background: radial-gradient(ellipse at 50% 55%, var(--sign-red-light) 0%, var(--sign-red) 70%);
    font-family: "Titan One", sans-serif;
  }
  .sign--wide { top: 270px; }
  .sign--stacked { top: 710px; }

  .brand-name {
    position: absolute;
    color: var(--letter-fill);
    font-size: 34px;
    line-height: 1;
    letter-spacing: 2px;
  }
  .headline {
    position: absolute;
    color: var(--letter-fill);
    line-height: 1;
    white-space: nowrap;
    -webkit-text-stroke: 6px var(--letter-stroke);
    paint-order: stroke fill;
    text-shadow: 0 0 14px var(--glow), 0 0 26px var(--glow);
  }

  .sign--wide .brand-name {
    left: 0; right: 0;
    top: 42px;
    text-align: center;
  }
  .sign--wide .headline {
    left: 0; right: 0;
    top: 112px;
    text-align: center;
    font-size: 92px;
    letter-spacing: 2px;
  }

  .sign--stacked .brand-name {
    left: 228px;
    top: 50px;
  }
  .sign--stacked .headline--top {
    left: 416px;
    top: 20px;
    font-size: 84px;
  }
  .sign--stacked .headline--bottom {
    left: 222px;
    top: 118px;
    font-size: 84px;
    letter-spacing: -3px;
  }
</style>
</head>
<body>
  <main class="canvas">
    <section class="sign sign--wide" aria-label="On the air sign, single line">
      <span class="brand-name">QTRM</span>
      <h1 class="headline">ON THE AIR</h1>
    </section>

    <section class="sign sign--stacked" aria-label="On the air sign, stacked">
      <span class="brand-name">QTRM</span>
      <p class="headline headline--top">ON</p>
      <p class="headline headline--bottom">THE AIR</p>
    </section>
  </main>
</body>
</html>
```